Tandle Repair - Handyman and Home Repair Services

I need a business card/letterhead logo for my new handyman service in my local area. I'm happy for a logo design to be done prior to business card design so it can be incorporated on to the card, for which I'd be happy to pay more for. I'd like it to be modern and not using the typical pictures of tools and cartoon characters in dungarees! I like the idea of tools but in a more modern way i.e subtle background images in different shades to main colour. I do like the american retro designs and those that show age and patina for example, having an image half old, half new in its appearance to represent the repairing of things. Colours in mind are 1950's retro colours, ie using grey with pastel greens, red and cream. I'd like to break the mould and the stigma thats attached to these jobs and make it more cool and up to date. I hope this will attract interior designers and more modern businesses to use my services.

This is the logo design I like and would be happy for this idea and colours:

http://toast-a-roam.co.uk/wp-content/uploads/2011/01/t-r_logo600px.png

```html
<!DOCTYPE html>
<html lang="en">
<head>
<meta charset="utf-8">
<title>Tandle Repair – Business Card</title>
<link rel="stylesheet" href="https://fonts.googleapis.com/css2?family=Yesteryear&display=swap">
<style>
  :root {
    --page: #ffffff;
    --card: #a9afae;
    --card-edge: #f3f2c9;
    --maroon: #4a0a08;
    --green: #12573a;
    --outline: #ffffff;
    --drop: #111111;
  }
  html, body {
    margin: 0;
    padding: 0;
    width: 1200px;
    height: 1000px;
    overflow: hidden;
    background: var(--page);
  }
  .canvas {
    position: relative;
    width: 1200px;
    height: 1000px;
  }
  .card {
    position: absolute;
    left: 258px;
    width: 684px;
    height: 436px;
    background: var(--card);
    border: 6px solid var(--card-edge);
    border-radius: 46px;
    overflow: hidden;
    font-family: "Yesteryear", cursive;
  }
  .card--front { top: 28px; }
  .card--back  { top: 532px; }

  .script {
    position: absolute;
    left: 0;
    width: 100%;
    text-align: center;
    margin: 0;
    white-space: nowrap;
    font-weight: 400;
    text-shadow:
      -1.5px -1.5px 0 var(--outline), 1.5px -1.5px 0 var(--outline),
      -1.5px 1.5px 0 var(--outline), 1.5px 1.5px 0 var(--outline),
      -4px 4px 0 var(--drop);
  }
  .owner-name {
    top: 58px;
    font-size: 66px;
    color: var(--maroon);
  }
  .owner-phone {
    top: 166px;
    font-size: 64px;
    letter-spacing: 3px;
    color: var(--green);
  }
  .owner-web {
    top: 276px;
    font-size: 70px;
    color: var(--maroon);
    text-shadow: none;
  }

  .brand-name {
    position: absolute;
    top: 110px;
    left: 0;
    width: 100%;
    margin: 0;
    text-align: center;
    font-size: 96px;
    font-weight: 400;
    color: var(--green);
    white-space: nowrap;
  }

  .tagline {
    font-size: 58px;
    color: var(--maroon);
    width: auto;
    transform-origin: left center;
  }
  .tagline--first {
    left: 44px;
    top: 280px;
    transform: rotate(-9deg);
  }
  .tagline--second {
    left: 170px;
    top: 330px;
    transform: rotate(-9deg);
  }
</style>
</head>
<body>
<main class="canvas">
  <section class="card card--front" aria-label="Card front">
    <p class="script owner-name">Owen Harlow</p>
    <p class="script owner-phone">07700 900418</p>
    <p class="script owner-web">www.tandlerepair.co.uk</p>
  </section>

  <section class="card card--back" aria-label="Card back">
    <h1 class="brand-name">Tandle Repair</h1>
    <p class="script tagline tagline--first">Handyman Services</p>
    <p class="script tagline tagline--second">from Repair to Install</p>
  </section>
</main>
</body>
</html>
```